Strategy and Technology Consulting - Our Story and Values Page

Interior Page design – Our History and Our Values

Our homepage has been designed and we are looking for a design for one of the interior pages. This interior page tells the story of Our History and Our Values

Because the homepage has been designed, we would like this interior page to reflect the design of the homepage without being a mirror image of the homepage.

This site will be implemented in WordPress using the Elementor framework.

Font: Poppins medium and Poppins dark
Illustrations: Our homepage illustrations were designed by “Welmo 1974” on Pixaborne. Compatible original or stock illustrations are welcome. Stock photography is also welcome. Welmo is also available through Welmo Trastek on Folivane

Uploaded Files
• Homepage design – this is the design we will use for our homepage. Contest entries should reflect this basic style but should be distinctly different from the homepage.
• Our History and Our Values – Wireframe – the basic layout of the page we are looking for.
• Our History and Our Values – Word document with the text supporting the wireframe.
• Color Palette – please use colors compatible with the palette attached.

Our Story - timeline
There is a timeline element in the wireframe. The wireframe displays this as a series of chevrons (arrows), but it does not need to be. Creativity in display of the timeline is appreciated.

Our Values
If you look at the Word document, you will see that there are a lot of words on the page. The winning design will present the information in a way that engages the user without overwhelming them with too much to read. For example, they may click on a value and see more information.

Target Market(s)

CIO's and Technology Executives

Number of Pages Required

1 page

Font styles to use
Sans Serif
Other font styles liked:
• Poppin

Requirements
Must have
• A timeline element, all of our values
Nice to have
• Clever timeline display

```html
<!DOCTYPE html>
<html lang="en">
<head>
<meta charset="utf-8">
<title>Our Story and Values – Veltrion</title>
<link rel="stylesheet" href="https://fonts.googleapis.com/css2?family=Poppins:wght@400;500;600;700;800&family=Rubik:wght@400;500&display=swap">
<style>
:root{
  --navy:#3f5070;
  --navy-dark:#3a4a66;
  --ink:#3d4b63;
  --text:#4b566a;
  --yellow:#f5c343;
  --yellow-deep:#f0b51f;
  --pale-blue:#e9f1fa;
  --grey-cell:#f1f3f6;
  --line:#d8dee7;
  --white:#ffffff;
}
*{box-sizing:border-box;margin:0;padding:0}
html,body{width:1200px;height:3677px;overflow:hidden}
body{position:relative;background:var(--white);font-family:"Rubik",sans-serif;color:var(--text)}
.abs{position:absolute}
.heading-font{font-family:"Poppins",sans-serif}

/* header */
.site-header{left:0;top:0;width:1200px;height:79px;border-bottom:1px solid #eef1f5;background:var(--white);z-index:3}
.brand{left:110px;top:18px;font-family:"Poppins",sans-serif;font-weight:400;font-size:38px;color:#8a94a6;letter-spacing:.5px;display:flex;align-items:center;gap:8px}
.brand-dot{width:10px;height:10px;background:var(--navy);border-radius:50%}
.main-nav{left:610px;top:30px;display:flex;gap:24px;font-family:"Poppins",sans-serif;font-size:11px;font-weight:500;color:var(--ink);align-items:center}
.main-nav span::after{content:" ⌄";font-size:10px}
.main-nav .home-icon::after{content:""}
.btn-yellow{background:var(--yellow-deep);color:var(--white);font-family:"Poppins",sans-serif;font-weight:700;font-size:11px;border-radius:20px;display:flex;align-items:center;justify-content:center;letter-spacing:.3px}
.header-cta{left:979px;top:23px;width:111px;height:32px}

/* hero */
.hero-title{left:110px;top:180px;font-family:"Poppins",sans-serif;font-weight:700;font-size:54px;line-height:58px;color:var(--ink)}
.hero-text{left:110px;top:318px;width:420px;font-size:15px;line-height:25px;color:var(--text)}
.hero-art{left:590px;top:136px;width:533px;height:285px;border-radius:6px;background:linear-gradient(135deg,#cfe0f4,#3f5fa0 70%,#f5c343)}

/* section headings */
.section-title{left:0;width:1200px;text-align:center;font-family:"Poppins",sans-serif;font-weight:700;font-size:48px;color:var(--ink);letter-spacing:.5px}
.section-title em{font-style:normal;color:var(--yellow)}
.section-rule{left:491px;width:228px;height:4px;background:var(--yellow);border-radius:2px}

/* timeline */
.tl-bar{left:528px;top:661px;width:26px;height:542px;background:var(--yellow)}
.tl-icon{width:134px;height:134px;border-radius:50%;border:3px solid #b9c6d6;background:var(--pale-blue);box-shadow:inset 0 0 0 8px #fff}
.tl-dash{left:395px;width:129px;border-top:2px dashed #aab6c6}
.tl-link{left:554px;width:96px;height:3px;background:var(--yellow)}
.tl-node{left:648px;width:20px;height:20px;border-radius:50%;border:3px solid var(--yellow);background:#fff}
.tl-year{left:689px;font-family:"Poppins",sans-serif;font-weight:600;font-size:26px;color:var(--ink)}
.tl-list{left:691px;list-style:none;font-size:15px;color:var(--text)}
.tl-list li{height:30px;display:flex;align-items:center;gap:10px}
.tick{width:15px;height:15px;border-radius:50%;background:var(--yellow);position:relative;flex:none}
.tick::after{content:"";position:absolute;left:5px;top:3px;width:4px;height:7px;border:solid #fff;border-width:0 2px 2px 0;transform:rotate(45deg)}
.tl-list .sub{padding-left:24px}

/* values */
.value-cell{width:600px}
.cell-grey{background:var(--grey-cell)}
.value{width:390px}
.value h3{font-family:"Poppins",sans-serif;font-weight:700;font-size:34px;color:var(--ink);position:relative;line-height:40px;margin-bottom:14px}
.value h3::before{content:"";position:absolute;left:-19px;top:0;width:4px;height:38px;background:var(--yellow)}
.value p{font-size:15px;line-height:24px;color:var(--text)}

/* newsletter + footer */
.footer-bg{left:0;top:2990px;width:1200px;height:687px}
.newsletter{left:138px;top:2965px;width:924px;height:206px;border-radius:103px;background:var(--yellow-deep)}
.newsletter h2{position:absolute;left:80px;top:52px;font-family:"Poppins",sans-serif;font-weight:800;font-size:32px;color:#fff}
.newsletter p{position:absolute;left:80px;top:108px;width:420px;font-family:"Poppins",sans-serif;font-size:15px;line-height:20px;color:#fff}
.news-field{position:absolute;left:549px;top:82px;width:320px;height:48px;background:#fff;border-radius:24px;display:flex;align-items:center;padding-left:22px;gap:10px;font-size:13px;color:#9aa3b1}
.news-send{position:absolute;right:6px;top:6px;width:36px;height:36px;border-radius:50%;background:#aebbcc}
.footer-brand{left:121px;top:3350px;font-family:"Poppins",sans-serif;font-weight:400;font-size:62px;color:#fff;display:flex;align-items:center;gap:10px}
.footer-brand .brand-dot{width:14px;height:14px;background:var(--yellow)}
.socials{left:176px;top:3429px;display:flex;gap:11px}
.socials span{width:40px;height:40px;border-radius:50%;background:rgba(255,255,255,.18)}
.footer-cta{left:215px;top:3493px;width:131px;height:38px}
.foot-col h4{font-family:"Poppins",sans-serif;font-weight:700;font-size:19px;color:#fff;margin-bottom:18px}
.foot-col ul{list-style:none;font-family:"Poppins",sans-serif;font-size:12.5px;color:#e6ebf2}
.foot-col li{height:31px}
.foot-col li::before{content:"›  "}
.contact-item{display:flex;gap:10px;font-family:"Poppins",sans-serif;font-size:12.5px;line-height:18px;color:#e6ebf2;margin-bottom:20px}
.contact-item svg{flex:none;margin-top:2px}
.copyright{left:0;top:3618px;width:1200px;height:59px;background:#344259;color:#fff;font-family:"Poppins",sans-serif;font-size:13px;display:flex;align-items:center;justify-content:center}
.chat{left:1134px;top:3590px;width:50px;height:50px;border-radius:50%;background:var(--yellow-deep);display:flex;align-items:center;justify-content:center}
</style>
</head>
<body>

<!-- background curves -->
<svg class="abs" style="left:0;top:79px" width="1200" height="1300" aria-hidden="true">
  <path d="M620 0 C700 120 720 260 880 330 C990 380 1080 420 1200 510 L1200 0 Z" fill="#e8f0f9"/>
  <path d="M0 490 C80 560 150 700 130 830 C100 780 50 720 0 700 Z" fill="#f2f6fb"/>
  <path d="M1200 610 C1120 700 1060 860 1090 1000 C1130 1120 1170 1150 1200 1160 Z" fill="#f2f6fb"/>
</svg>

<header class="abs site-header">
  <div class="abs brand"><span class="brand-dot"></span>Veltrion</div>
  <nav class="abs main-nav">
    <svg class="home-icon" width="14" height="12" viewBox="0 0 14 12"><path d="M7 0 L14 6 H12 V12 H8.5 V8 H5.5 V12 H2 V6 H0 Z" fill="#8fa0b6"/></svg>
    <span>ABOUT US</span><span>SERVICES</span><span>INSIGHTS</span><span>JOIN US</span>
  </nav>
  <div class="abs btn-yellow header-cta">CONTACT US</div>
</header>

<h1 class="abs hero-title">Our Story and<br>Values</h1>
<p class="abs hero-text">Since 2015, We have been providing customers with the highest quality floor coatings and sealers. With Stonecrest Custom Flooring, we bring life to areas you use the most.</p>
<div class="abs hero-art" role="img" aria-label="Illustration of a business team meeting around a table with a presenter at a chart board"></div>

<h2 class="abs section-title" style="top:537px">OUR <em>STORY</em></h2>
<div class="abs section-rule" style="top:612px"></div>

<div class="abs tl-bar"></div>
<svg class="abs" style="left:528px;top:650px" width="26" height="12" aria-hidden="true"><path d="M0 12 L13 0 L26 12 Z" fill="var(--yellow)"/></svg>
<svg class="abs" style="left:528px;top:1202px" width="26" height="12" aria-hidden="true"><path d="M0 0 L13 12 L26 0 Z" fill="var(--yellow)"/></svg>

<div class="abs tl-icon" style="left:258px;top:689px" role="img" aria-label="Icon of growth chart with money and plant"></div>
<div class="abs tl-icon" style="left:258px;top:885px" role="img" aria-label="Icon of light bulb made of puzzle pieces"></div>
<div class="abs tl-icon" style="left:258px;top:1079px" role="img" aria-label="Icon of person climbing a rising bar chart"></div>

<div class="abs tl-dash" style="top:755px"></div>
<div class="abs tl-dash" style="top:951px"></div>
<div class="abs tl-dash" style="top:1146px"></div>

<div class="abs tl-link" style="top:754px"></div><div class="abs tl-node" style="top:746px"></div>
<div class="abs tl-link" style="top:950px"></div><div class="abs tl-node" style="top:942px"></div>
<div class="abs tl-link" style="top:1145px"></div><div class="abs tl-node" style="top:1137px"></div>

<div class="abs tl-year" style="top:736px">2017 – 2019</div>
<ul class="abs tl-list" style="top:776px">
  <li><span class="tick"></span>Growth Strategy Focus</li>
  <li><span class="tick"></span>Consistent, Modest Growth</li>
  <li><span class="tick"></span>Preliminary Focus on Technology</li>
  <li><span class="tick"></span>Eureka!&nbsp; Implementing strategy is hard.</li>
</ul>

<div class="abs tl-year" style="top:932px">2020 – 2021</div>
<ul class="abs tl-list" style="top:972px">
  <li><span class="tick"></span>Pandemic Pauses Growth</li>
  <li><span class="tick"></span>Rethinking</li>
  <li class="sub">-&nbsp; The business model</li>
  <li class="sub">-&nbsp; The delivery model</li>
</ul>

<div class="abs tl-year" style="top:1129px">2022 and Onward</div>
<ul class="abs tl-list" style="top:1169px">
  <li><span class="tick"></span>Leadership Team for Focus on Essential Areas</li>
  <li><span class="tick"></span>Rapid Growth</li>
  <li><span class="tick"></span>Preliminary Focus on Technology</li>
  <li><span class="tick"></span>Customer Success</li>
</ul>

<!-- values grid -->
<div class="abs value-cell cell-grey" style="left:0;top:1399px;height:442px"></div>
<div class="abs value-cell cell-grey" style="left:598px;top:1841px;height:367px;width:602px"></div>
<div class="abs value-cell cell-grey" style="left:0;top:2208px;height:351px"></div>

<h2 class="abs section-title" style="top:1450px">OUR <em>VALUE</em></h2>
<div class="abs section-rule" style="top:1524px"></div>

<article class="abs value" style="left:160px;top:1598px">
  <h3>Regardless</h3>
  <p>Each person's unique experiences and perspectives add vibrant hues to the tapestry of our shared existence.&nbsp; In a world where diversity paints the canvas of humanity, true beauty is found in recognizing the inherent and incalculable value of every human being.</p>
</article>
<article class="abs value" style="left:673px;top:1586px;width:395px">
  <h3>Collaboration</h3>
  <p>Collaboration in work transforms individual endeavors into symphonies of collective achievement. Through collaboration, diverse talents converge, fostering a rich exchange of ideas that amplifies creativity, accelerates progress, and brings forth solutions beyond what a single mind could conceive.</p>
</article>
<article class="abs value" style="left:160px;top:1940px;width:380px">
  <h3>Passion</h3>
  <p>Passion infuses our work with energy, transforming routine tasks into opportunities for creativity and innovation. Fueled by passion, individuals become unstoppable forces, driven to overcome challenges and achieve remarkable outcomes that benefit them and inspire those around them</p>
</article>
<article class="abs value" style="left:673px;top:1928px;width:395px">
  <h3>Excellence</h3>
  <p>Excellence isn't a destination; it's a continuous journey of refinement and growth. Striving for excellence cultivates a culture of continuous improvement, fostering innovation, credibility, and a lasting impact that resonates far beyond the immediate task.</p>
</article>
<article class="abs value" style="left:160px;top:2309px;width:385px">
  <h3>Tenacity</h3>
  <p>Tenacity is the unwavering anchor that keeps us grounded amidst adversity, propelling us forward when faced with obstacles. The resilience to persist, adapt, and learn from setbacks leads to the mastery of skills and the fulfillment of ambitious goals.</p>
</article>
<article class="abs value" style="left:673px;top:2297px;width:390px">
  <h3>Solution Mindset</h3>
  <p>A solution mindset is the compass that directs our focus from problems to possibilities. It empowers us to navigate challenges with a proactive mindset, igniting a journey of exploration and innovation that not only resolves issues but also paves the way for continuous growth and success.</p>
</article>
<article class="abs value" style="left:160px;top:2641px;width:385px">
  <h3>Generosity</h3>
  <p>Generosity creates a virtuous cycle of goodwill, fostering a sense of unity and shared purpose among colleagues. By freely sharing knowledge, support, and resources, we uplift those around us and contribute to a collaborative environment where collective achievements flourish.</p>
</article>

<!-- footer -->
<svg class="abs footer-bg" viewBox="0 0 1200 687" preserveAspectRatio="none" aria-hidden="true">
  <defs><linearGradient id="footGrad" x1="0" y1="1" x2="1" y2="0"><stop offset="0" stop-color="#6a7f99"/><stop offset=".55" stop-color="#46577a"/><stop offset="1" stop-color="#3b4b68"/></linearGradient></defs>
  <path d="M0 0 C140 60 220 240 330 200 C420 170 470 150 560 200 C660 260 760 300 860 250 C960 200 1040 100 1200 110 L1200 687 L0 687 Z" fill="#dfe3e9"/>
  <path d="M0 15 C140 75 220 260 330 220 C420 190 470 175 560 225 C660 285 760 325 860 275 C960 225 1040 120 1200 130 L1200 687 L0 687 Z" fill="url(#footGrad)"/>
</svg>

<section class="abs newsletter">
  <h2>Subscribe Our Newsletter</h2>
  <p>Subscribe our newsletter to receive the latest news and exclusive offers every week, No spam.</p>
  <div class="news-field">
    <svg width="14" height="10" viewBox="0 0 14 10"><rect width="14" height="10" rx="1" fill="#aab4c2"/><path d="M0 0 L7 6 L14 0" stroke="#fff" fill="none"/></svg>
    Enter email address
    <span class="news-send"><svg width="36" height="36" viewBox="0 0 36 36"><path d="M11 18 L25 11 L21 25 L18 20 Z" fill="#fff"/></svg></span>
  </div>
</section>

<div class="abs footer-brand"><span class="brand-dot"></span>Veltrion</div>
<div class="abs socials"><span></span><span></span><span></span><span></span></div>
<div class="abs btn-yellow footer-cta">CONTACT US</div>

<div class="abs foot-col" style="left:491px;top:3326px">
  <h4>Quick links</h4>
  <ul><li>Home</li><li>About Us</li><li>Services</li><li>Insights</li><li>Join Us</li><li>Contact Us</li></ul>
</div>
<div class="abs foot-col" style="left:668px;top:3326px">
  <h4>Our Services</h4>
  <ul><li>Business Transformation</li><li>ERP Implementations</li><li>ERP Solutions</li><li>BI and Data</li><li>Building the Right Team...</li></ul>
</div>
<div class="abs foot-col" style="left:899px;top:3326px;width:190px">
  <h4>Contact info</h4>
  <div class="contact-item"><svg width="14" height="10" viewBox="0 0 14 10"><rect width="14" height="10" rx="1" fill="var(--yellow)"/><path d="M0 0 L7 6 L14 0" stroke="#46577a" fill="none"/></svg><div>Email:<br>hello@veltrionmail.com</div></div>
  <div class="contact-item"><svg width="14" height="14" viewBox="0 0 14 14"><path d="M3 0 L5 4 L3.5 5.5 C4.5 8 6 9.5 8.5 10.5 L10 9 L14 11 L13 14 C6 14 0 8 0 1 Z" fill="var(--yellow)"/></svg><div>Phone:<br>+44 100 555 0192</div></div>
  <div class="contact-item"><svg width="12" height="16" viewBox="0 0 12 16"><path d="M6 0 C9.3 0 12 2.6 12 6 C12 10 6 16 6 16 C6 16 0 10 0 6 C0 2.6 2.7 0 6 0 Z" fill="var(--yellow)"/><circle cx="6" cy="6" r="2.3" fill="#46577a"/></svg><div>Location:<br>Some address line goes here city name</div></div>
</div>

<div class="abs copyright">© Veltrion Design 2023, All Rights Reserved</div>
<div class="abs chat"><svg width="26" height="22" viewBox="0 0 26 22"><path d="M13 1 C20 1 25 5 25 10 C25 15 20 19 13 19 L6 22 L7 17 C3 15 1 13 1 10 C1 5 6 1 13 1 Z" fill="#fff"/><circle cx="8" cy="10" r="1.6" fill="var(--yellow-deep)"/><circle cx="13" cy="10" r="1.6" fill="var(--yellow-deep)"/><circle cx="18" cy="10" r="1.6" fill="var(--yellow-deep)"/></svg></div>

</body>
</html>
```